KESTREL Communications Business Card- Belsa

Kestrel Integrated Communications is Corporate communications agency with more than 20 years of experience. We become part of the manegement team of our clients in other to improve their outcomes and grow the possitioning of their brand.
We are in Puerto Rico, latin caribbean island
Name: Maribelsa (Belsa) Ocampo
787-555-0148
bocampo@kestrelwing.example

Target Market(s)

finance and pharmaceutical companies

Industry/Entity Type

Business

Contact Information for Business Card

modern, edgy colorful and playfull like our logo

Requirements
Must have
• company logo
• name
• tel
• email

```html
<!DOCTYPE html>
<html lang="en">
<head>
<meta charset="utf-8">
<title>KESTREL Communications – Business Card</title>
<link rel="stylesheet" href="https://fonts.googleapis.com/css2?family=Lato:wght@400;700;900&display=swap">
<style>
  :root {
    --stage: #2b2b2b;
    --orange: #ea5a1f;
    --orange-light: #f26a2a;
    --brown: #3a2410;
    --paper: #fbfbfb;
    --ink: #333333;
    --rule: #b9b2ab;
    --map-tint: #f6d9cb;
  }
  * { box-sizing: border-box; margin: 0; padding: 0; }
  html, body {
    width: 1200px; height: 873px; overflow: hidden;
    background: var(--stage);
    font-family: "Lato", Arial, sans-serif;
  }
  .canvas {
    position: relative; width: 1200px; height: 873px;
    display: flex; align-items: center; justify-content: center; gap: 60px;
  }
  .card {
    position: relative; width: 520px; height: 300px; border-radius: 18px; overflow: hidden;
  }
  .card--back {
    background: linear-gradient(135deg, var(--orange-light), var(--orange));
  }
  .card--back .brand {
    position: absolute; left: 60px; right: 60px; top: 100px;
    text-align: center; color: #ffffff;
    font-weight: 900; font-size: 34px; line-height: 1.15; letter-spacing: 1px;
  }
  .card--back .website {
    position: absolute; right: 34px; bottom: 26px;
    color: #ffffff; font-weight: 700; font-size: 13px; letter-spacing: 3px;
  }
  .card--front { background: var(--paper); }
  .card--front .world-map {
    position: absolute; left: 40px; top: 60px; width: 440px; height: 190px;
    border-radius: 40px;
    background: radial-gradient(ellipse at center, var(--map-tint) 0%, rgba(246,217,203,0.3) 60%, rgba(246,217,203,0) 100%);
  }
  .card--front .brand {
    position: absolute; left: 20px; width: 200px; top: 128px;
    text-align: center; color: var(--brown);
    font-weight: 900; font-size: 22px; line-height: 1.2; letter-spacing: 0.5px;
  }
  .card--front .divider {
    position: absolute; left: 240px; top: 40px; width: 2px; height: 220px;
    background: linear-gradient(to bottom, rgba(185,178,171,0), var(--rule) 40%, var(--rule) 60%, rgba(185,178,171,0));
  }
  .contact {
    position: absolute; left: 262px; top: 52px; right: 14px; color: var(--ink);
  }
  .contact .name {
    color: var(--orange); font-weight: 700; font-size: 14px; line-height: 1.2; white-space: nowrap;
  }
  .contact .role { font-size: 12.5px; margin-top: 8px; }
  .contact ul { list-style: none; margin-top: 30px; }
  .contact li {
    display: flex; align-items: flex-start; gap: 9px;
    font-size: 12px; line-height: 1.3; margin-bottom: 8px; white-space: nowrap;
  }
  .contact .icon { flex: 0 0 18px; width: 18px; height: 18px; }
</style>
</head>
<body>
<main class="canvas">
  <section class="card card--back" aria-label="Card back">
    <div class="brand">KESTREL<br>Communications</div>
    <div class="website">www.kestrelwing.example</div>
  </section>

  <section class="card card--front" aria-label="Card front">
    <div class="world-map" role="img" aria-label="Faint dotted world map in the background"></div>
    <div class="brand">KESTREL<br>Communications</div>
    <div class="divider"></div>
    <div class="contact">
      <p class="name">Maribelsa (Belsa) Ocampo Arroyo</p>
      <p class="role">Owner / Founder</p>
      <ul>
        <li>
          <svg class="icon" viewBox="0 0 18 18" aria-hidden="true">
            <circle cx="9" cy="9" r="9" fill="var(--orange)"/>
            <path d="M6 4.5c.5-.3 1-.2 1.3.3l.9 1.6c.2.4.1.8-.2 1.1l-.6.5c.5 1.1 1.3 1.9 2.4 2.4l.5-.6c.3-.3.7-.4 1.1-.2l1.6.9c.5.3.6.8.3 1.3l-.5.8c-.4.6-1.1.8-1.800.6C8.4 12.4 5.6 9.6 4.8 7c-.2-.7 0-1.4.6-1.8z" fill="#fff"/>
          </svg>
          <span>787-555-0148</span>
        </li>
        <li>
          <svg class="icon" viewBox="0 0 18 18" aria-hidden="true">
            <circle cx="9" cy="9" r="9" fill="var(--orange)"/>
            <rect x="4.5" y="6" width="9" height="6.5" rx="1" fill="none" stroke="#fff" stroke-width="1.2"/>
            <path d="M4.8 6.4 9 9.6l4.2-3.2" fill="none" stroke="#fff" stroke-width="1.2"/>
          </svg>
          <span>bocampo@kestrelwing.example</span>
        </li>
        <li>
          <svg class="icon" viewBox="0 0 18 18" aria-hidden="true">
            <circle cx="9" cy="9" r="9" fill="var(--orange)"/>
            <path d="M9 4a3.2 3.2 0 0 0-3.2 3.2C5.8 9.6 9 13.6 9 13.6s3.2-4 3.2-6.4A3.2 3.2 0 0 0 9 4z" fill="#fff"/>
            <circle cx="9" cy="7.2" r="1.2" fill="var(--orange)"/>
          </svg>
          <span>450 Harbor Lane, Villa Serena<br>Bayamar, Puerto Rico 00961</span>
        </li>
      </ul>
    </div>
  </section>
</main>
</body>
</html>
```